Etiketten für Imkerei aus der Steiermark
Zielgruppe
Wir sind eine Imkerei aus der Steiermark / Österreich im Vollerwerb. www.talmann-biene.at
Zielgruppe: Frauen, Familien, Regional
Unser Image: hohe Qualität, Familienbetrieb, naturnah, gesund
Vermarktung: Direkt, Verkaufsstellen, Märkte, zukünftig auch online
Aufgabenstellung
Wir werden die Honiggläser und die Druckerei umstellen und möchten hierfür ein profesionelles abgestimmtes Design. Unser Logo soll erhalten bleiben. Die Honigsortenbezeichnung (Waldhonig, Cremehonig, Blütenhonig) soll zukünftig eingedruckt werden und neben dem Logo ein Zentrales Element sein.
In Zukunft verwenden wir Vintra Gläser mit hohen Deckel der Firma Glasoria in den Größen 1000g(Lise 785), 500g (Vin 410), 250 g (Vin 212) und 150 g (Vin 125). Der Deckel soll einheitlich Gold oder Silber sein.

```html
<!DOCTYPE html>
<html lang="de">
<head>
<meta charset="utf-8">
<title>Talmann Biene – Etiketten Waldhonig</title>
<link href="https://fonts.googleapis.com/css2?family=Playfair+Display:wght@400;700&display=swap" rel="stylesheet">
<style>
  :root {
    --page: #ffffff;
    --ink-gold: #7a6a45;
    --ink-dark: #1d1a12;
    --ink-light: #ffffff;
    --label-white: #ffffff;
    --label-brown: #857650;
    --label-green: #00802f;
    --logo-yellow: #fbf09a;
  }
  * { margin: 0; padding: 0; box-sizing: border-box; }
  html, body { width: 1200px; height: 979px; overflow: hidden; background: var(--page); }
  body { position: relative; font-family: "Playfair Display", serif; }

  .label {
    position: absolute;
    left: 333px;
    width: 534px;
    height: 163px;
    box-shadow: 0 14px 30px rgba(0,0,0,0.18);
    color: var(--ink-light);
    overflow: hidden;
  }
  .label--white { top: 155px; background: var(--label-white); color: var(--ink-gold); }
  .label--brown { top: 407px; background: var(--label-brown); }
  .label--green { top: 659px; background: var(--label-green); }

  .comb-field {
    position: absolute;
    left: 130px; top: 0;
    width: 275px; height: 163px;
    background: radial-gradient(ellipse at center, rgba(255,255,255,0.16) 0%, rgba(255,255,255,0.06) 55%, rgba(255,255,255,0) 75%);
  }
  .label--white .comb-field {
    background: radial-gradient(ellipse at center, rgba(122,106,69,0.10) 0%, rgba(122,106,69,0.04) 55%, rgba(122,106,69,0) 75%);
  }

  .weight {
    position: absolute; left: 92px; top: 10px; width: 100px; margin-left: -50px;
    text-align: center; font-size: 6.5px; letter-spacing: 1.5px;
  }

  .variety {
    position: absolute; left: 9px; top: 72px; width: 160px; height: 24px;
    border: 0.6px solid currentColor;
    text-align: center; font-size: 19px; line-height: 23px; letter-spacing: 3px;
  }
  .storage {
    position: absolute; left: 9px; top: 100px; width: 160px;
    text-align: center; font-size: 3.8px; line-height: 6px; letter-spacing: 0.5px;
    font-weight: 700; text-transform: uppercase;
  }

  .brand {
    position: absolute; left: 211px; top: 30px; width: 110px; height: 102px;
    display: flex; flex-direction: column; align-items: center; justify-content: center;
    background: var(--logo-yellow);
    border: 3px solid var(--ink-light);
  }
  .label--white .brand { border-color: rgba(122,106,69,0.5); border-width: 0.6px; }
  .brand-dot { width: 10px; height: 10px; border-radius: 50%; background: var(--ink-dark); margin-bottom: 6px; }
  .brand-name {
    color: var(--ink-dark); font-weight: 700; font-size: 17px; line-height: 18px; text-align: center;
  }

  .quality {
    position: absolute; left: 185px; top: 141px; width: 156px; height: 9px;
    border: 0.5px solid currentColor;
    text-align: center; font-size: 5.5px; line-height: 8px; letter-spacing: 1px;
  }

  .producer {
    position: absolute; left: 402px; top: 63px; width: 120px; text-align: center;
  }
  .producer-title { font-size: 5.8px; letter-spacing: 1.6px; margin-bottom: 6px; }
  .producer-contact { font-size: 3.8px; line-height: 6px; letter-spacing: 0.9px; font-weight: 700; text-transform: uppercase; }
</style>
</head>
<body>

  <section class="label label--white">
    <div class="comb-field" role="img" aria-label="Dezentes Wabenmuster"></div>
    <div class="weight">1000 G</div>
    <div class="variety">WALDHONIG</div>
    <div class="storage">Trocken und vor Wärme geschützt lagern.<br>Mindestens haltbar bis:</div>
    <div class="brand"><span class="brand-dot"></span><span class="brand-name">Talmann<br>Biene</span></div>
    <div class="quality">ÖSTERREICHISCHER QUALITÄTSHONIG</div>
    <div class="producer">
      <div class="producer-title">MEISTERIMKEREI TALMANN</div>
      <div class="producer-contact">Martina &amp; Georg<br>Hollgraben 27<br>8124 Übelbach<br>T. 0664 / 31 47 592<br>post@talmann-biene.at<br>www.talmann-biene.at</div>
    </div>
  </section>

  <section class="label label--brown">
    <div class="comb-field" role="img" aria-label="Dezentes Wabenmuster"></div>
    <div class="weight">1000 G</div>
    <div class="variety">WALDHONIG</div>
    <div class="storage">Trocken und vor Wärme geschützt lagern.<br>Mindestens haltbar bis:</div>
    <div class="brand"><span class="brand-dot"></span><span class="brand-name">Talmann<br>Biene</span></div>
    <div class="quality">ÖSTERREICHISCHER QUALITÄTSHONIG</div>
    <div class="producer">
      <div class="producer-title">MEISTERIMKEREI TALMANN</div>
      <div class="producer-contact">Martina &amp; Georg<br>Hollgraben 27<br>8124 Übelbach<br>T. 0664 / 31 47 592<br>post@talmann-biene.at<br>www.talmann-biene.at</div>
    </div>
  </section>

  <section class="label label--green">
    <div class="comb-field" role="img" aria-label="Dezentes Wabenmuster"></div>
    <div class="weight">1000 G</div>
    <div class="variety">WALDHONIG</div>
    <div class="storage">Trocken und vor Wärme geschützt lagern.<br>Mindestens haltbar bis:</div>
    <div class="brand"><span class="brand-dot"></span><span class="brand-name">Talmann<br>Biene</span></div>
    <div class="quality">ÖSTERREICHISCHER QUALITÄTSHONIG</div>
    <div class="producer">
      <div class="producer-title">MEISTERIMKEREI TALMANN</div>
      <div class="producer-contact">Martina &amp; Georg<br>Hollgraben 27<br>8124 Übelbach<br>T. 0664 / 31 47 592<br>post@talmann-biene.at<br>www.talmann-biene.at</div>
    </div>
  </section>

</body>
</html>
```